TR Stationery - Modern Contemporary

Develop modern template for Letterhead and Stationery (business card, letterhead, envelopes) using the TR Logo and Icon

Colors
0054AA
0677BA
7BADD7
CADEEF
E8F1F8
00AB8E
00BBA5
67D7C9
C6EFE9
E9F9F6
EE7325
F08F49
F5BC92
FAE3D3
FDF4ED
6B429C
8869AF
B7A5CE
E3DAEB
F3F0F8

```html
<!DOCTYPE html>
<html lang="en">
<head>
<meta charset="utf-8">
<title>Terra Rivo Letterhead</title>
<link href="https://fonts.googleapis.com/css2?family=Source+Sans+3:wght@400;600&display=swap" rel="stylesheet">
<style>
  :root {
    --backdrop: #e9eaec;
    --paper: #ffffff;
    --navy: #2a2f4a;
    --green: #36b873;
    --orange: #ee7325;
    --ink: #4a4a4a;
    --ink-strong: #3a3a3a;
    --signature-fill: #eceef3;
  }
  * { margin: 0; padding: 0; box-sizing: border-box; }
  html, body { width: 1154px; height: 1200px; overflow: hidden; background: var(--backdrop); }
  body { font-family: "Source Sans 3", Arial, sans-serif; color: var(--ink); }
  .letterhead {
    position: absolute; left: 148px; top: 0;
    width: 857px; height: 1200px;
    background: var(--paper); overflow: hidden;
  }
  .brand {
    position: absolute; top: 62px; left: 0; right: 0;
    display: flex; justify-content: center; align-items: center; gap: 10px;
  }
  .brand-name { font-size: 42px; font-weight: 400; color: var(--navy); letter-spacing: 1px; line-height: 1; }
  .brand-dot { width: 9px; height: 9px; border-radius: 50%; background: var(--orange); }
  .sender { position: absolute; left: 66px; top: 322px; }
  .sender-name { font-size: 16px; color: var(--ink-strong); margin-bottom: 3px; }
  .sender-line { font-size: 12.5px; line-height: 21px; }
  .body-copy {
    position: absolute; left: 66px; top: 425px; width: 726px;
    font-size: 12.6px; line-height: 21px; text-align: justify;
  }
  .body-copy p + p { margin-top: 18px; }
  .closing { position: absolute; left: 66px; top: 759px; font-size: 13.5px; }
  .signature { position: absolute; left: 64px; top: 786px; width: 176px; height: 40px; }
  .footer-wave { position: absolute; left: 0; top: 1000px; width: 857px; height: 200px; }
  .contact {
    position: absolute; left: 0; right: 0; top: 1144px;
    display: flex; justify-content: center; gap: 18px;
    color: #fff; font-size: 15px;
  }
  .contact-item { display: flex; align-items: center; gap: 6px; }
  .contact-item svg { width: 12px; height: 12px; }
  .address {
    position: absolute; left: 0; right: 0; top: 1166px;
    display: flex; justify-content: center; align-items: center; gap: 6px;
    color: #fff; font-size: 15px;
  }
  .address-rule { width: 103px; height: 1px; background: #fff; }
</style>
</head>
<body>
  <main class="letterhead">
    <header class="brand">
      <span class="brand-name">terra rivo</span>
      <span class="brand-dot"></span>
    </header>

    <section class="sender">
      <div class="sender-name">DARIEN HOLLOWAY</div>
      <div class="sender-line">President / CEO</div>
      <div class="sender-line">City/State, Zip Code</div>
    </section>

    <section class="body-copy">
      <p>Lorem Ipsum is simply dummy text of the printing and typesetting industry. Lorem Ipsum has been the industry's standard dummy text ever since the 1500s, when an unknown printer took a galley of type and scrambled it to make a type specimen book. It has survived not only five centuries, but also the leap into electronic typesetting, remaining essentially unchanged. It was popularised in the 1960s with the release of Typeline sheets containing Lorem Ipsum passages, and more recently with desktop publishing software like Pagecraft Studio including versions of Lorem Ipsum.</p>
      <p>It is a long established fact that a reader will be distracted by the readable content of a page when looking at its layout. The point of using Lorem Ipsum is that it has a more-or-less normal distribution of letters, as opposed to using 'Content here, content here', making it look like readable English. Many desktop publishing packages and web page editors now use Lorem Ipsum as their default model text, and a searchaccident, sometimes on purpose (injected humour and the like).</p>
      <p>There are many variations of passages of Lorem Ipsum available, but the majority have suffered alteration in some form, by injected humour, or randomised words which don't look even slightly believable. If you are going to use a passage of Lorem Ipsum, you need to be sure there isn't anything embarrassing hidden in the middle of text.</p>
    </section>

    <div class="closing">Sincerely,</div>
    <svg class="signature" role="img" aria-label="Handwritten signature of the sender" viewBox="0 0 176 40">
      <rect width="176" height="40" rx="4" fill="var(--signature-fill)"/>
    </svg>

    <svg class="footer-wave" viewBox="0 0 857 200" preserveAspectRatio="none" aria-hidden="true">
      <path d="M0,48 C120,110 470,128 825,28 C480,122 160,128 0,78 Z" fill="var(--green)"/>
      <path d="M0,83 C160,140 470,140 857,22 L857,200 L0,200 Z" fill="var(--navy)"/>
    </svg>

    <div class="contact">
      <span class="contact-item">
        <svg viewBox="0 0 24 24"><path fill="#ee7325" d="M6.6 10.8a15 15 0 0 0 6.6 6.6l2.2-2.2c.3-.3.7-.4 1-.2 1.1.4 2.3.6 3.6.6.6 0 1 .4 1 1V20c0 .6-.4 1-1 1A17 17 0 0 1 3 4c0-.6.4-1 1-1h3.5c.6 0 1 .4 1 1 0 1.3.2 2.5.6 3.6.1.3 0 .7-.2 1z"/></svg>
        300.555.0147
      </span>
      <span class="contact-item">
        <svg viewBox="0 0 24 24"><path fill="#ee7325" d="M2 5h20v14H2z"/><path fill="none" stroke="#2a2f4a" stroke-width="2" d="M2 5l10 8 10-8"/></svg>
        hello@terrarivo.com
      </span>
      <span class="contact-item">
        <svg viewBox="0 0 24 24"><circle cx="12" cy="12" r="10" fill="#ee7325"/><path fill="none" stroke="#2a2f4a" stroke-width="1.5" d="M2 12h20M12 2c3 3 3 17 0 20M12 2c-3 3-3 17 0 20"/></svg>
        www.terrarivo.com
      </span>
    </div>
    <div class="address">
      <span class="address-rule"></span>
      <span>418 Alder Lane, Fairview, CO 80999</span>
      <span class="address-rule"></span>
    </div>
  </main>
</body>
</html>
```